Yard sign design for high end luxury home builder.

Need a design for signage on custom homes that are being built. I already have a logo that I am satisfied with that needs to be incorporated. I need the following incorporated in the design of the sign-
- Lic number 582316
- phone number (805) 471-2938‬
- tembleyhomeworks.com
- Logo/Branding

If possible it may be nice to have the following quote that is on are business cards-

Quote from Corwin of Valdema-
HE WHO WORKS WITH HIS HANDS IS A LABORER.
HE WHO WORKS WITH HIS HANDS & HIS HEAD IS A CRAFTSMAN.
HE WHO WORKS WITH HIS HANDS & HIS HEAD & HIS HEART IS AN ARTISAN.
-CORWIN OF VALDEMA

Target Market(s)

Archetect, Designers, Clients desiring to build a new home or remodel.

Colors
fde9d4
fee4d5
fabb94
fac994
faa54b
f68d4d
f37122
f78f20
f68e4e

Requirements
Must have
• - Lic number 582316
• - phone number (805) 471-2938‬
• - tembleyhomeworks.com
• - Logo/Branding
Nice to have
• Quote from Corwin of Valdema-
• HE WHO WORKS WITH HIS HANDS IS A LABORER.
• HE WHO WORKS WITH HIS HANDS & HIS HEAD IS A CRAFTSMAN.
• HE WHO WORKS WITH HIS HANDS & HIS HEAD & HIS HEART IS AN ARTISAN.
• -CORWIN OF VALDEMA
• OR the below statement-
• Craftsmen that Care
Should not have
• Any additional verbiage not specified above including any type of verbiage about what kind of company we are. For instance- Integrity, reputable... It's just all played out. Im just looking for a bitching design that has the info that compliments my logo/branding.

```html
<!DOCTYPE html>
<html lang="en">
<head>
<meta charset="utf-8">
<title>Tembley Homeworks Inc. — Yard Sign</title>
<link rel="stylesheet" href="https://fonts.googleapis.com/css2?family=Michroma&family=Oswald:wght@600;700&display=swap">
<style>
  :root {
    --page: #ffffff;
    --band: #000000;
    --brand-tan: #b3a07f;
    --accent-orange: #f37122;
    --text-white: #ffffff;
    --photo-warm: #4a3626;
    --photo-deep: #1c140e;
  }
  * { margin: 0; padding: 0; box-sizing: border-box; }
  html, body {
    width: 1200px; height: 1004px; overflow: hidden;
    background: var(--page);
  }
  .sign {
    position: absolute; left: 183px; top: 225px;
    width: 850px; height: 566px;
    background: var(--band); overflow: hidden;
  }
  .sign__header {
    position: absolute; left: 0; top: 0; width: 100%; height: 84px;
    background: var(--band); z-index: 2;
  }
  .brand {
    position: absolute; left: 31px; top: 24px;
    font-family: "Oswald", sans-serif; font-weight: 600;
    color: var(--brand-tan); font-size: 28px; line-height: 36px;
    letter-spacing: 1px; white-space: nowrap;
  }
  .social {
    position: absolute; top: 22px; width: 42px; height: 42px;
  }
  .social--first { left: 655px; }
  .social--second { left: 775px; }
  .photo {
    position: absolute; left: 0; top: 84px; width: 100%; height: 482px;
    background:
      linear-gradient(180deg, rgba(0,0,0,0) 0%, rgba(0,0,0,0.15) 45%, rgba(0,0,0,0.85) 62%, rgba(0,0,0,0.9) 100%),
      radial-gradient(ellipse at 45% 15%, var(--photo-warm) 0%, var(--photo-deep) 70%);
  }
  .quote {
    position: absolute; left: 32px; top: 184px; width: 810px;
    font-family: "Oswald", sans-serif; font-weight: 700;
    color: var(--text-white); font-size: 50px; line-height: 63px;
    letter-spacing: 1.8px; z-index: 2;
  }
  .quote__line { display: block; white-space: nowrap; }
  .quote__author {
    position: absolute; right: 33px; top: 315px;
    font-family: "Oswald", sans-serif; font-weight: 700;
    font-size: 21px; letter-spacing: 0.6px; color: var(--text-white); z-index: 2;
  }
  .contact {
    position: absolute; left: 0; width: 100%; text-align: center;
    white-space: nowrap; z-index: 2;
  }
  .contact__web {
    top: 362px; font-family: "Michroma", sans-serif;
    color: var(--accent-orange); font-size: 32px; letter-spacing: 1.5px;
    -webkit-text-stroke: 1.6px var(--accent-orange);
  }
  .contact__license {
    top: 407px; font-family: "Michroma", sans-serif;
    color: var(--accent-orange); font-size: 27px; letter-spacing: 1.5px;
    -webkit-text-stroke: 1.4px var(--accent-orange);
  }
  .contact__phone {
    top: 466px; font-family: "Oswald", sans-serif; font-weight: 700;
    color: var(--text-white); font-size: 68px; line-height: 1;
    letter-spacing: 4px;
  }
</style>
</head>
<body>
  <div class="sign">
    <header class="sign__header">
      <div class="brand">TEMBLEY HOMEWORKS INC.</div>
      <svg class="social social--first" viewBox="0 0 42 42" aria-hidden="true">
        <circle cx="21" cy="21" r="18" fill="none" stroke="#ffffff" stroke-width="3"/>
      </svg>
      <svg class="social social--second" viewBox="0 0 42 42" aria-hidden="true">
        <circle cx="21" cy="21" r="18" fill="none" stroke="#ffffff" stroke-width="3"/>
      </svg>
    </header>

    <div class="photo" role="img" aria-label="Photo of a builder framing a house with a power drill among wooden studs"></div>

    <p class="quote">
      <span class="quote__line">He who works with his hands</span>
      <span class="quote__line">&amp; his head &amp; his heart is an artisan</span>
    </p>
    <p class="quote__author">Corwin of Valdema</p>

    <p class="contact contact__web">TEMBLEYHOMEWORKS.COM</p>
    <p class="contact contact__license">License #582316</p>
    <p class="contact contact__phone">(805) 471-2938</p>
  </div>
</body>
</html>
```